New Website - vostimo.net

This is what we looking for - http://www.craftlane-example.com/design/583017
Updates

hello, im back and i want some good designs for my website.. i need really creative ideas. this is for a cellphone provider company. Vostimo mobile please provide me a good ideas and i will go with u also to program the website

Font styles to use
Sans Serif

```html
<!DOCTYPE html>
<html lang="en">
<head>
<meta charset="utf-8">
<title>Vostimo Communications</title>
<link href="https://fonts.googleapis.com/css2?family=Open+Sans:wght@300;400;600;700&family=Raleway:wght@500&family=Ubuntu:wght@400;500;700&display=swap" rel="stylesheet">
<style>
:root{
  --bg:#ececec;
  --blue:#1e8fd8;
  --blue-light:#4fb3ee;
  --ink:#333;
  --text:#555;
  --dark:#1c1c1c;
  --footer:#333333;
  --panel:#fafafa;
  --line:#dcdcdc;
}
*{box-sizing:border-box;margin:0;padding:0}
html,body{width:1138px;height:1200px;overflow:hidden}
body{background:var(--bg);font-family:Arial,Helvetica,sans-serif;color:var(--text);position:relative}
.abs{position:absolute}

.brand{left:96px;top:26px;display:flex;align-items:center;gap:12px}
.brand-dot{width:52px;height:52px;border-radius:50%;background:var(--blue-light)}
.brand-name{font-family:"Ubuntu",sans-serif;font-size:44px;font-weight:400;color:var(--blue-light);line-height:1}
.brand-sub{font-family:"Ubuntu",sans-serif;font-size:15px;letter-spacing:2.6px;color:#444;margin-top:4px}

.search{left:820px;top:31px;width:221px;height:28px;background:#fff;border:1px solid #ddd;border-radius:3px;font-size:11px;color:#999;padding:7px 8px}
.search svg{position:absolute;right:7px;top:6px}

.tabs{left:102px;top:112px;display:flex;gap:14px}
.tab{height:40px;background:linear-gradient(#fff,#f0f0f0);border:1px solid #d6d6d6;border-bottom:none;border-radius:6px 6px 0 0;font-family:"Ubuntu",sans-serif;font-size:17px;color:#333;display:flex;align-items:center;justify-content:center}
.tab-home{width:101px}.tab-office{width:96px}.tab-cell{width:120px;margin-left:-3px}

.utility{left:775px;top:108px;font-size:13px;color:#333;display:flex;gap:22px;align-items:center}
.utility .caret{width:17px;height:16px;border:1px solid #bbb;background:#f5f5f5;border-radius:2px;margin-left:-14px;display:flex;align-items:center;justify-content:center}

.hero{left:102px;top:151px;width:941px;height:347px;background:var(--dark);border-radius:0 6px 6px 6px;overflow:hidden}
.hero-photo{left:560px;top:30px;width:370px;height:317px;background:radial-gradient(ellipse at 65% 45%,#7a6b60 0%,#4a4440 45%,#1c1c1c 75%);z-index:1}
.hero-title{left:25px;top:64px;font-family:"Raleway",sans-serif;font-size:32px;color:var(--blue);font-weight:500;white-space:nowrap;z-index:2}
.hero-sub{left:25px;top:117px;font-family:"Open Sans",sans-serif;font-weight:300;font-size:25px;color:#e6e6e6;line-height:35px;z-index:2}
.hero-btn{left:24px;top:216px;width:225px;height:46px;border-radius:12px;background:linear-gradient(#f4f4f4,#bdbdbd);font-family:"Ubuntu",sans-serif;font-weight:500;font-size:25px;color:#444;display:flex;align-items:center;justify-content:center;letter-spacing:1px;box-shadow:0 2px 3px rgba(0,0,0,.6);z-index:2}

.card{background:var(--panel);border:1px solid var(--line);border-radius:3px;box-shadow:0 1px 2px rgba(0,0,0,.05)}
.about{left:102px;top:517px;width:941px;height:258px}
.video{left:16px;top:17px;width:325px;height:218px;background:linear-gradient(135deg,#c9d6e0,#8a99a6 60%,#e4e8ea);border:2px solid #ccc}
.video-bar{position:absolute;left:0;bottom:0;width:100%;height:18px;background:#2a2a2a}
.video-bar .prog{position:absolute;left:66px;top:6px;width:62px;height:6px;background:#3f7ed6}
.video-bar .vol{position:absolute;left:220px;top:6px;width:26px;height:6px;background:#3f7ed6}
.play{position:absolute;left:130px;top:60px}
.about-title{left:361px;top:20px;font-family:"Ubuntu",sans-serif;font-size:22px;font-weight:400;color:var(--blue)}
.about-text{left:361px;top:55px;width:560px;font-size:12.4px;line-height:21px;color:#444;text-align:justify}
.about-text p+p{margin-top:21px}

.feature{top:805px;width:291px;height:231px}
.f1{left:102px}.f2{left:427px}.f3{left:752px}
.feature h2{position:absolute;left:16px;top:12px;font-family:"Ubuntu",sans-serif;font-weight:400;font-size:31px;color:var(--blue);letter-spacing:.5px}
.feature h3{position:absolute;left:16px;top:56px;font-size:13px;font-weight:700;color:#444}
.feature ul{position:absolute;left:18px;top:84px;list-style:none;font-size:12px;color:#444}
.feature li{height:26.5px;padding-left:14px;position:relative}
.feature li:before{content:"";position:absolute;left:0;top:5px;width:5px;height:5px;border-radius:50%;background:#555}
.feature .more{position:absolute;left:16px;top:199px;font-size:13px;font-style:italic;color:var(--blue);text-decoration:underline}
.keep{position:absolute;left:27px;top:83px;font-size:16px;font-weight:700;color:#222;letter-spacing:.5px}
.fields{position:absolute;left:26px;top:117px;display:flex;gap:13px}
.fields span{width:71px;height:29px;background:#fff;border:1px solid #ccc}
.check{position:absolute;left:29px;top:162px;width:209px;height:39px;background:linear-gradient(#2a9ae6,#0b66b8);border:1px solid #0a5aa0;font-size:20px;font-weight:700;color:#fff;display:flex;align-items:center;justify-content:center}

.footer{left:0;top:1072px;width:1138px;height:128px;background:var(--footer)}
.f-brand{left:104px;top:33px;display:flex;align-items:center;gap:12px}
.f-brand .brand-dot{width:48px;height:48px;background:#999}
.f-brand .brand-name{color:#aaa;font-size:40px}
.f-brand .brand-sub{color:#ccc;font-size:14px}
.divider{top:10px;width:0;height:112px;border-left:1px dashed #555}
.f-nav{left:458px;top:35px;display:flex;gap:25px;font-size:11.5px;font-weight:700;color:#ccc}
.f-nav span:before{content:"";display:inline-block;border-left:4px solid #ccc;border-top:4px solid transparent;border-bottom:4px solid transparent;margin-right:10px}
.f-copy{left:475px;top:69px;font-size:11.5px;font-weight:700;color:#ccc}
.follow{left:950px;top:14px;font-size:12.5px;font-weight:700;color:#ddd}
.socials{left:926px;top:38px;display:flex;gap:8px}
.socials span{width:29px;height:29px;border-radius:50%;background:#2f6fb8;border:2px solid #dfe8f2}
.phone{left:860px;top:78px;display:flex;align-items:center;gap:10px;font-family:"Ubuntu",sans-serif;font-size:26px;color:#eee;letter-spacing:1px}
</style>
</head>
<body>

<div class="abs brand">
  <span class="brand-dot"></span>
  <div><div class="brand-name">Vostimo</div><div class="brand-sub">COMMUNICATIONS</div></div>
</div>

<div class="abs search">Search here...
  <svg width="14" height="14" viewBox="0 0 14 14"><circle cx="6" cy="6" r="4.5" fill="none" stroke="#999" stroke-width="1.6"/><line x1="9.3" y1="9.3" x2="13" y2="13" stroke="#999" stroke-width="1.8"/></svg>
</div>

<nav class="abs tabs">
  <div class="tab tab-home">Home</div>
  <div class="tab tab-office">Office</div>
  <div class="tab tab-cell">Cellphone</div>
</nav>

<div class="abs utility">
  <span>Support</span><span>|</span><span>Contact</span><span>|</span><span>My Account</span>
  <span class="caret"><svg width="8" height="5"><polygon points="0,0 8,0 4,5" fill="#555"/></svg></span>
</div>

<section class="abs hero">
  <div class="abs hero-photo" role="img" aria-label="Support agent with headset beside a desk phone"></div>
  <h1 class="abs hero-title">A Revolutionary Digital Phone Service</h1>
  <p class="abs hero-sub">that will Save you, your family, &amp; Your<br>Business lots of Money</p>
  <div class="abs hero-btn">Sign Up Today</div>
</section>

<section class="abs card about">
  <div class="abs video" role="img" aria-label="Video still of a call centre team at work">
    <svg class="play" width="66" height="66" viewBox="0 0 66 66"><circle cx="33" cy="33" r="31" fill="#222" stroke="#ddd" stroke-width="3"/><polygon points="25,18 25,48 50,33" fill="#fff"/></svg>
    <div class="video-bar"><span class="prog"></span><span class="vol"></span></div>
  </div>
  <h2 class="abs about-title">About Us</h2>
  <div class="abs about-text">
    <p>Lorem ipsum dolor sit amet, consectetur adipisicing elit, sed do eiusmod tempor incididunt ut labore et dolore magna aliqua. Ut enim ad minim veniam, quis nostrud exercitation ullamco laboris commodo consequat.</p>
    <p>Duis aute irure dolor in reprehenderit in voluptate velit esse cillum dolore eu fugiat nulla pariatur. Excepteur sint occaecat cupidatat non proident, sunt in culpa qui officia deserunt mollit anim id est laborum. pariatur. Stet clita kasd gubergren, no sea takimata est. Excepteur sint occaecat cupidatat non proident, sunt in culpa qui officia deserunt mollit anim id est laborum. pariatur sunt in culpa qui. Stet clita kasd gubergren, no sea takimata est.</p>
  </div>
</section>

<section class="abs card feature f1">
  <h2>Affordable</h2>
  <h3>Starting Saving Today!</h3>
  <ul><li>simply dummy text of the printing</li><li>Lorem Ipsum has been the industry's</li><li>Lorem Ipsum has been the industry's</li><li>Lorem Ipsum has been the industry's</li></ul>
  <span class="more">Compare rates &amp; Plans ›</span>
</section>

<section class="abs card feature f2">
  <h2>Powerful</h2>
  <h3>Incredible Features, Standard</h3>
  <ul><li>simply dummy text of the printing</li><li>Lorem Ipsum has been the industry's</li><li>Lorem Ipsum has been the industry's</li><li>Lorem Ipsum has been the industry's</li></ul>
  <span class="more">Compare rates &amp; Plans</span>
</section>

<section class="abs card feature f3">
  <h2 style="left:26px">Flexible</h2>
  <h3 style="left:26px;top:57px">Service On Your Own Terms</h3>
  <div class="keep">KEEP YOUR NAME</div>
  <div class="fields"><span></span><span></span><span></span></div>
  <div class="check">Check Availability</div>
</section>

<footer class="abs footer">
  <div class="abs f-brand">
    <span class="brand-dot"></span>
    <div><div class="brand-name">Vostimo</div><div class="brand-sub">COMMUNICATIONS</div></div>
  </div>
  <div class="abs divider" style="left:352px"></div>
  <div class="abs divider" style="left:813px"></div>
  <div class="abs f-nav"><span>Home</span><span>Products</span><span>News</span><span>Contact</span></div>
  <div class="abs f-copy">Vostimo Communication © Copyright-2012-13</div>
  <div class="abs follow">Follow Us On</div>
  <div class="abs socials"><span></span><span></span><span></span></div>
  <div class="abs phone">
    <svg width="34" height="34" viewBox="0 0 34 34"><circle cx="17" cy="17" r="15" fill="none" stroke="#eee" stroke-width="2.5"/><path d="M12 9c1-1 2 0 3 2s0 3-1 4c1 2 2 3 4 4 1-1 2-2 4-1s3 2 2 3c-1 2-3 3-5 2-4-2-7-5-9-9-1-2 0-4 2-5z" fill="#eee"/></svg>
    5550142378
  </div>
</footer>

</body>
</html>
```